Just to be clear - I have the domain and the wordpress site (which is messy). I need someone to help me complete a simple blog design and then go into the existing wordpress site, and get rid of all the existing rubbish and set up the templates please. If we progress with design can we please be clear about additional costs upfront which, of course, I appreciate is the case.

Need a lifestyle blog. It is called brightyearsahead.com. Aimed at the older woman but needs to look fresh and young, not old fashioned. Navigation will be Home, Fashion, Feelings, Fitness, Contact. I have a logo but not sure it will work at the moment so happy with stylised words.Will have social media links.

Need homepage (not overly long) to have a main slider for pics/videos. Then the three category boxes underneath linking through to 2nd level pages containing blogs for that category and then the actual blog page. Happy to be led by expertise if this is not gonna work.

Am really looking for something clean and fresh like a Marvette type approach to be honest.

If you need any further direction please just ask - once design chosen I am looking to move quickly.

Thank you so much for looking at this brief

Target Market(s)

Women, 40 - 60 age group but with a younger outlook

Colors

Requirements
Must have
• Reflect youth, fun, bright
• Lift easily into a wordpress format
Should not have
• Old, staid, frumpy,dark

```html
<!DOCTYPE html>
<html lang="en">
<head>
<meta charset="utf-8">
<title>Bright Years Ahead — Homepage and Fitness Blog</title>
<link rel="stylesheet" href="https://fonts.googleapis.com/css2?family=Oswald:wght@400;500&family=Poppins:wght@500;600&family=Open+Sans:wght@400;600&display=swap">
<style>
:root{
  --stage:#213a5c;
  --teal:#1b9a7e;
  --teal-dark:#15806a;
  --white:#ffffff;
  --ink:#2b2b2b;
  --muted:#8a8a8a;
  --paper:#f1f1f1;
  --line:#e3e3e3;
  --star:#f2a93b;
  --hero-dark:#1e1c1a;
  --hero-warm:#5a4a3c;
}
*{box-sizing:border-box;margin:0;padding:0}
html,body{width:1200px;height:3758px;overflow:hidden}
body{background:var(--stage);font-family:"Open Sans",Arial,sans-serif;color:var(--ink);position:relative}

.page{position:absolute;left:84px;width:1032px;overflow:hidden;background:var(--paper);box-shadow:0 10px 30px rgba(0,0,0,.35)}
.page--home{top:646px;height:1017px}
.page--blog{top:1766px;height:1891px}

/* header */
.site-header{position:absolute;left:0;top:0;width:100%;height:110px;z-index:5;display:flex;align-items:center;justify-content:space-between;padding:0 62px 0 112px}
.brand{display:flex;align-items:center;gap:10px;font-family:"Oswald",sans-serif;font-weight:500;font-size:30px;color:var(--white);letter-spacing:.5px}
.brand-mark{width:14px;height:14px;background:var(--teal)}
.main-nav{display:flex;gap:38px}
.main-nav a{font-family:"Poppins",sans-serif;font-weight:600;font-size:14px;color:var(--white);text-decoration:none;letter-spacing:.6px}

/* hero */
.hero-photo{position:absolute;left:0;top:0;width:100%;background:radial-gradient(ellipse at 30% 45%,#9a7a62 0%,var(--hero-warm) 28%,var(--hero-dark) 65%),var(--hero-dark)}
.page--home .hero-photo{height:560px;background:radial-gradient(ellipse at 30% 45%,#a27f63 0%,#5a4a3c 30%,#1e1c1a 68%),radial-gradient(circle at 90% 30%,#6b6256 0%,transparent 40%)}
.page--blog .hero-photo{height:420px}
.slide-caption{position:absolute;left:611px;top:222px;z-index:4}
.slide-title{font-family:"Oswald",sans-serif;font-weight:400;font-size:31px;line-height:44px;color:var(--white);text-transform:uppercase}
.btn-pill{display:inline-block;margin-top:28px;width:115px;height:31px;line-height:31px;text-align:center;border-radius:16px;background:var(--teal);color:var(--white);font-family:"Oswald",sans-serif;font-size:13px;text-transform:uppercase}
.slider-dots{display:flex;gap:8px;margin-top:22px}
.slider-dots span{width:13px;height:13px;border-radius:50%;border:2px solid var(--white)}
.slider-dots span.is-active{background:var(--teal);border-color:var(--teal)}
.hero-edge{position:absolute;left:0;width:100%;z-index:3}

/* category tiles */
.category-tiles{position:absolute;left:0;top:470px;width:100%;height:391px;display:flex}
.category-tile{flex:1;position:relative}
.category-tile + .category-tile{border-left:3px solid var(--white)}
.category-tile--fashion{background:linear-gradient(160deg,#b99c86,#6e4f43 60%,#3b2c2a)}
.category-tile--feelings{background:linear-gradient(180deg,#8f8a7a,#c9c4bd 55%,#6a87b0)}
.category-tile--fitness{background:linear-gradient(170deg,#7fa35a,#b9c4a8 50%,#4a7a3a)}
.category-label{position:absolute;left:0;bottom:112px;width:100%;height:40px;line-height:40px;text-align:center;background:rgba(25,25,25,.72);color:var(--white);font-family:"Poppins",sans-serif;font-weight:600;font-size:18px;letter-spacing:1px;text-transform:uppercase}

/* footer */
.site-footer{position:absolute;left:0;bottom:0;width:100%;background:var(--teal);text-align:center;color:var(--white);font-family:"Poppins",sans-serif}
.page--home .site-footer{height:156px}
.page--blog .site-footer{height:150px}
.footer-nav{padding-top:40px;font-size:13px}
.footer-nav a{color:var(--white);text-decoration:none}
.footer-nav .sep{margin:0 7px}
.copyright{margin-top:12px;font-size:13px}
.social-links{display:flex;justify-content:center;gap:5px;margin-top:12px}
.social-links span{width:17px;height:17px;border-radius:50%;border:1.5px solid var(--white)}

/* blog page */
.page-badge{position:absolute;left:666px;top:206px;z-index:5;width:250px;height:48px;line-height:48px;text-align:center;background:var(--teal);color:var(--white);font-family:"Oswald",sans-serif;font-weight:500;font-size:28px;letter-spacing:1px;text-transform:uppercase}
.post-list{position:absolute;left:113px;top:358px;width:558px;z-index:4;display:flex;flex-direction:column;gap:23px}
.post-card{display:flex;height:230px;background:var(--white);box-shadow:0 1px 4px rgba(0,0,0,.12)}
.post-thumb{width:245px;flex:none}
.thumb-1{background:linear-gradient(160deg,#cfd9a3,#8fae6a 60%,#506b3a)}
.thumb-2{background:linear-gradient(170deg,#6a5a50,#3a3432 60%,#2b4f73)}
.thumb-3{background:linear-gradient(180deg,#d2e2ec,#a3b8a0 55%,#5c8a3e)}
.thumb-4{background:linear-gradient(160deg,#8fb7d6,#e6c8b2 50%,#c8a273)}
.thumb-5{background:linear-gradient(170deg,#c98b8b,#a6544c 50%,#e4d0c6)}
.post-body{padding:18px 22px 0 22px}
.post-title{font-family:"Poppins",sans-serif;font-weight:500;font-size:15.5px;line-height:21px;color:var(--ink)}
.post-meta{display:flex;gap:26px;margin-top:18px;font-size:10px;color:var(--muted);font-style:italic}
.post-meta span{display:flex;align-items:center;gap:5px}
.post-excerpt{margin-top:10px;font-size:9.5px;line-height:14px;color:var(--muted)}
.btn-small{display:inline-block;margin-top:14px;padding:0 8px;height:19px;line-height:19px;background:var(--teal);color:var(--white);font-family:"Poppins",sans-serif;font-size:9px;text-transform:uppercase}
.pagination{position:absolute;left:196px;top:1648px;display:flex;gap:5px;font-size:9.5px;z-index:4}
.pagination span{min-width:20px;height:18px;line-height:18px;padding:0 6px;text-align:center;background:var(--white);border:1px solid var(--line)}

.sidebar{position:absolute;left:706px;top:361px;width:210px;z-index:4;display:flex;flex-direction:column;gap:14px}
.widget{background:var(--white);box-shadow:0 1px 4px rgba(0,0,0,.12)}
.widget-title{height:30px;line-height:30px;padding-left:8px;background:var(--teal);color:var(--white);font-family:"Poppins",sans-serif;font-weight:600;font-size:13px;text-transform:uppercase}
.widget--community{height:338px}
.widget--recent{height:438px}
.widget--categories{height:210px}
.member{display:flex;align-items:center;gap:10px;padding:22px 0 0 16px}
.member + .member{padding-top:26px}
.avatar{width:64px;height:64px;border-radius:50%;border:3px solid var(--line);background:radial-gradient(circle at 50% 40%,#c8a48a,#7a6455)}
.member-name,.recent-title{font-size:11px;color:var(--ink);line-height:14px}
.member-text{font-size:11px;color:var(--ink);line-height:14px}
.stars{color:var(--star);font-size:9px;letter-spacing:1px}
.stars i{color:#cfcfcf;font-style:normal}
.recent-post{display:flex;gap:12px;padding:22px 10px 0 10px}
.recent-post + .recent-post{border-top:1px solid var(--line);margin-top:16px}
.recent-thumb{width:80px;height:82px;flex:none}
.rt-1{background:linear-gradient(160deg,#9bc27a,#3f6a3a)}
.rt-2{background:linear-gradient(170deg,#dfeaf0,#b7c9c0)}
.rt-3{background:linear-gradient(170deg,#5d7fb8,#c7c2b3)}
.recent-text{font-size:9px;line-height:12px;color:var(--muted);margin-top:2px}
.recent-comments{font-size:9px;color:var(--muted);font-style:italic;margin-top:8px}
.category-list{list-style:none;padding:10px 0 0 12px}
.category-list li{font-size:9.5px;line-height:20px;color:var(--ink)}
.video-feature{height:188px;position:relative;background:linear-gradient(170deg,#7aa35c,#d6c7a8 55%,#8f9c6a);display:flex;align-items:center;justify-content:center}
</style>
</head>
<body>

<!-- Homepage -->
<section class="page page--home" aria-label="Homepage">
  <div class="hero-photo" role="img" aria-label="Slider photo of a woman in sportswear looking over her shoulder, blurred city lights behind"></div>
  <header class="site-header">
    <div class="brand"><span class="brand-mark"></span>BRIGHT YEARS AHEAD</div>
    <nav class="main-nav"><a href="#">HOME</a><a href="#">FASHION</a><a href="#">FEELINGS</a><a href="#">FITNESS</a><a href="#">CONTACT</a></nav>
  </header>
  <div class="slide-caption">
    <h1 class="slide-title">Quis autem vel eum<br>iure reprehenderit qui</h1>
    <a class="btn-pill" href="#">Read more</a>
    <div class="slider-dots"><span class="is-active"></span><span></span><span></span></div>
  </div>

  <div class="category-tiles">
    <a class="category-tile category-tile--fashion" href="#" role="img" aria-label="Fashion photo of a smiling woman in a hat and knit poncho"><span class="category-label">Fashion</span></a>
    <a class="category-tile category-tile--feelings" href="#" role="img" aria-label="Feelings photo of a woman sitting relaxed on a mat outdoors"><span class="category-label">Feelings</span></a>
    <a class="category-tile category-tile--fitness" href="#" role="img" aria-label="Fitness photo of a woman stretching in a park"><span class="category-label">Fitness</span></a>
  </div>
  <svg class="hero-edge" style="top:450px" width="1032" height="90" viewBox="0 0 1032 90">
    <polygon points="0,0 1032,0 1032,12 870,38 700,42 430,62 300,58 90,25 0,12" fill="#221f1c"/>
    <polyline points="0,12 90,25 300,58 430,62 700,42 870,38 1032,12" fill="none" stroke="#ffffff" stroke-width="3"/>
  </svg>

  <footer class="site-footer">
    <nav class="footer-nav"><a href="#">Wallet</a><span class="sep">/</span><a href="#">Fashion</a><span class="sep">/</span><a href="#">Feelings</a><span class="sep">/</span><a href="#">Fitness</a><span class="sep">/</span><a href="#">Contact us</a></nav>
    <p class="copyright">Copyright © 2018 Bright Years Ahead. All rights reserved.</p>
    <div class="social-links"><span></span><span></span><span></span><span></span><span></span></div>
  </footer>
</section>

<!-- Fitness blog listing -->
<section class="page page--blog" aria-label="Fitness blog page">
  <div class="hero-photo" role="img" aria-label="Header photo of a woman in sportswear looking over her shoulder, blurred lights behind"></div>
  <header class="site-header">
    <div class="brand"><span class="brand-mark"></span>BRIGHT YEARS AHEAD</div>
    <nav class="main-nav"><a href="#">HOME</a><a href="#">FASHION</a><a href="#">FEELINGS</a><a href="#">FITNESS</a><a href="#">CONTACT</a></nav>
  </header>
  <h1 class="page-badge">Fitness Blog</h1>
  <svg class="hero-edge" style="top:360px" width="1032" height="70" viewBox="0 0 1032 70">
    <polygon points="0,40 140,52 520,62 1032,20 1032,70 0,70" fill="#f1f1f1"/>
    <polyline points="0,40 140,52 520,62 1032,20" fill="none" stroke="#1b9a7e" stroke-width="4"/>
  </svg>

  <div class="post-list">
    <article class="post-card">
      <div class="post-thumb thumb-1" role="img" aria-label="Woman stretching her arms outdoors in sunlight"></div>
      <div class="post-body">
        <h2 class="post-title">Nemo enim ipsam voluptatem quia voluptas sit aspernatur</h2>
        <div class="post-meta"><span>▦ Jan 25, 2018</span><span>◌ 2 comments</span><span>✎ by Elliot</span></div>
        <p class="post-excerpt">Sed ut perspiciatis unde omnis iste natus error sit voluptatem accusantium doloremque laudantium, totam rem aperiam, eaque ipsa quae ab illo inventore veritatis et quasi architecto beatae vitae dicta sunt explicabo. Nemo enim ipsam</p>
        <a class="btn-small" href="#">Read more →</a>
      </div>
    </article>
    <article class="post-card">
      <div class="post-thumb thumb-2" role="img" aria-label="Woman kneeling on a blue exercise mat in a gym"></div>
      <div class="post-body">
        <h2 class="post-title">Nemo enim ipsam voluptatem quia voluptas sit aspernatur</h2>
        <div class="post-meta"><span>▦ Jan 25, 2018</span><span>◌ 2 comments</span><span>✎ by Elliot</span></div>
        <p class="post-excerpt">Sed ut perspiciatis unde omnis iste natus error sit voluptatem accusantium doloremque laudantium, totam rem aperiam, eaque ipsa quae ab illo inventore veritatis et quasi architecto beatae vitae dicta sunt explicabo. Nemo enim ipsam</p>
        <a class="btn-small" href="#">Read more →</a>
      </div>
    </article>
    <article class="post-card">
      <div class="post-thumb thumb-3" role="img" aria-label="Woman doing a push-up on grass"></div>
      <div class="post-body">
        <h2 class="post-title">Nemo enim ipsam voluptatem quia voluptas sit aspernatur</h2>
        <div class="post-meta"><span>▦ Jan 25, 2018</span><span>◌ 2 comments</span><span>✎ by Elliot</span></div>
        <p class="post-excerpt">Sed ut perspiciatis unde omnis iste natus error sit voluptatem accusantium doloremque laudantium, totam rem aperiam, eaque ipsa quae ab illo inventore veritatis et quasi architecto beatae vitae dicta sunt explicabo. Nemo enim ipsam</p>
        <a class="btn-small" href="#">Read more →</a>
      </div>
    </article>
    <article class="post-card">
      <div class="post-thumb thumb-4" role="img" aria-label="Laughing woman holding a bowl of salad"></div>
      <div class="post-body">
        <h2 class="post-title">Nemo enim ipsam voluptatem quia voluptas sit aspernatur</h2>
        <div class="post-meta"><span>▦ Jan 25, 2018</span><span>◌ 2 comments</span><span>✎ by Elliot</span></div>
        <p class="post-excerpt">Sed ut perspiciatis unde omnis iste natus error sit voluptatem accusantium doloremque laudantium, totam rem aperiam, eaque ipsa quae ab illo inventore veritatis et quasi architecto beatae vitae dicta sunt explicabo. Nemo enim ipsam</p>
        <a class="btn-small" href="#">Read more →</a>
      </div>
    </article>
    <article class="post-card">
      <div class="post-thumb thumb-5" role="img" aria-label="Group of women doing plank exercises in a studio"></div>
      <div class="post-body">
        <h2 class="post-title">Nemo enim ipsam voluptatem quia voluptas sit aspernatur</h2>
        <div class="post-meta"><span>▦ Jan 25, 2018</span><span>◌ 2 comments</span><span>✎ by Elliot</span></div>
        <p class="post-excerpt">Sed ut perspiciatis unde omnis iste natus error sit voluptatem accusantium doloremque laudantium, totam rem aperiam, eaque ipsa quae ab illo inventore veritatis et quasi architecto beatae vitae dicta sunt explicabo. Nemo enim ipsam</p>
        <a class="btn-small" href="#">Read more →</a>
      </div>
    </article>
  </div>

  <nav class="pagination" aria-label="Pages"><span>Prev</span><span>1</span><span>2</span><span>3</span><span>4</span><span>5</span><span>6</span><span>…</span><span>22</span><span>Next</span></nav>

  <aside class="sidebar">
    <section class="widget widget--community">
      <h3 class="widget-title">Community</h3>
      <div class="member"><div class="avatar" role="img" aria-label="Member portrait"></div><div><p class="member-name">Nadia Ferrow</p><p class="member-text">Sed ut perspiciatis</p><p class="stars">★★★<i>★★</i></p></div></div>
      <div class="member"><div class="avatar" role="img" aria-label="Member portrait"></div><div><p class="member-name">Nadia Ferrow</p><p class="member-text">Sed ut perspiciatis</p><p class="stars">★★★<i>★★</i></p></div></div>
      <div class="member"><div class="avatar" role="img" aria-label="Member portrait"></div><div><p class="member-name">Nadia Ferrow</p><p class="member-text">Sed ut perspiciatis</p><p class="stars">★★★<i>★★</i></p></div></div>
    </section>
    <section class="widget widget--recent">
      <h3 class="widget-title">Recent posts</h3>
      <div class="recent-post"><div class="recent-thumb rt-1" role="img" aria-label="Woman exercising on grass"></div><div><p class="recent-title">Nemo enim ipsam</p><p class="stars">★★★<i>★★</i></p><p class="recent-text">Lorem ipsum dolor sit amet, consectetur</p><p class="recent-comments">◌ 2 comments</p></div></div>
      <div class="recent-post"><div class="recent-thumb rt-2" role="img" aria-label="Woman in a yoga pose"></div><div><p class="recent-title">Nemo enim ipsam</p><p class="stars">★★★<i>★★</i></p><p class="recent-text">Lorem ipsum dolor sit amet, consectetur</p><p class="recent-comments">◌ 2 comments</p></div></div>
      <div class="recent-post"><div class="recent-thumb rt-3" role="img" aria-label="Woman sitting and stretching"></div><div><p class="recent-title">Nemo enim ipsam</p><p class="stars">★★★<i>★★</i></p><p class="recent-text">Lorem ipsum dolor sit amet, consectetur</p><p class="recent-comments">◌ 2 comments</p></div></div>
    </section>
    <section class="widget widget--categories">
      <h3 class="widget-title">Categories</h3>
      <ul class="category-list"><li>June 2017</li><li>December 2010</li><li>November 2010</li><li>October 2010</li><li>September 2010</li><li>August 2010</li><li>May 2010</li></ul>
    </section>
    <div class="video-feature" role="img" aria-label="Video still of a woman exercising outdoors">
      <svg width="46" height="46" viewBox="0 0 46 46" aria-hidden="true"><circle cx="23" cy="23" r="21" fill="rgba(0,0,0,.25)" stroke="#ffffff" stroke-width="2"/><polygon points="18,14 33,23 18,32" fill="#ffffff"/></svg>
    </div>
  </aside>

  <footer class="site-footer">
    <nav class="footer-nav"><a href="#">Wallet</a><span class="sep">/</span><a href="#">Fashion</a><span class="sep">/</span><a href="#">Feelings</a><span class="sep">/</span><a href="#">Fitness</a><span class="sep">/</span><a href="#">Contact us</a></nav>
    <p class="copyright">Copyright © 2018 Bright Years Ahead. All rights reserved.</p>
    <div class="social-links"><span></span><span></span><span></span><span></span><span></span></div>
  </footer>
</section>

</body>
</html>
```